PSD Designs needed to give to my Developer

Hello, I need PSD files to give to my programmer for the creation of my new website. The website is for ZORVA lane, a new clothing company based in Chicago, IL. We sell womens, mens and kids fashion. We specialize in jackets, outerwear and sweaters, but we sell clothing from every category, I have someone working on the logo, so I can't include it for reference. However, I have included 2 reference sites as well as a PDF of how the 2 reference sites could be merged together. The main company color should be blue (hence the name ZORVA lane), and the overall feel of the site should be FUN. It should communicate: This is where you want to shop if you want a FUN, HAPPY experience. I need the Home Page file designed very quickly. Whoever is awarded this job will immediately continue working with me to design the other 8 pages. I will pay for all pages. The amount I am offering is for this one page only, and I will pay you additional to design all other 8 pages. Thank you for your time and I will be picking the best design so that we can immediately build a great relationship and work through the rest of the project.

Industry/Entity Type

Apparel Store

Number of Pages Required

1 page

Font styles to use
Sans Serif

Colors
33a6d7
0492cd
ffffff

Requirements
Must have
• I have included all notes in the project description so please check there. My project must communicate: Fun and Happy Design. Even tho I have chosen a few variations of blue below, I still want the designer to incorporate other colors as necessary to acheive the desired look.
Should not have
• It should have a boring, childish feel

```html
<!DOCTYPE html>
<html lang="en">
<head>
<meta charset="utf-8">
<title>ZORVA lane – Home</title>
<link rel="stylesheet" href="https://fonts.googleapis.com/css2?family=Roboto:wght@300;400;500;700&display=swap">
<style>
:root{
  --blue-strong:#0492cd;
  --blue-hero:#3a9bd5;
  --blue-card:#39a5d8;
  --blue-band:rgba(23,146,210,.85);
  --green:#4cb847;
  --green-btn:#8fdb7c;
  --yellow:#fdc94b;
  --yellow-btn:#fde08c;
  --sky-btn:#7fd4f5;
  --page:#f3f3f3;
  --white:#ffffff;
  --ink:#333333;
  --ink-soft:#555555;
  --field:#f4f4f4;
  --icon:#9a9a9a;
}
*{box-sizing:border-box;margin:0;padding:0}
html,body{width:879px;height:1200px;overflow:hidden}
body{position:relative;background:var(--page);font-family:'Roboto',sans-serif;color:var(--ink)}
.abs{position:absolute}

/* top bar */
.top-bar{left:0;top:0;width:879px;height:27px;background:var(--blue-strong);color:var(--white)}
.promo{left:63px;top:8px;font-size:10px;font-weight:500}
.social{top:7px;width:14px;height:14px;border-radius:50%;background:#25577a}
.login{left:751px;top:4px;width:70px;height:19px;border:1px solid var(--white);font-size:8px;font-weight:500;text-align:center;line-height:17px;letter-spacing:.2px}

/* header */
.nav{left:63px;top:63px;display:flex;gap:0;font-size:9px;text-transform:uppercase}
.nav a{color:var(--ink);text-decoration:none;margin-right:18px;padding:0 6px 4px 6px}
.nav a:first-child{margin-left:0;padding-left:6px}
.nav a.active{color:var(--blue-strong);border-bottom:1px solid #8bc34a}
.brand{left:700px;top:36px;width:135px;text-align:center;color:var(--blue-strong);font-weight:400;font-size:26px;line-height:30px;letter-spacing:1px}

/* hero */
.hero{left:63px;top:107px;width:757px;height:370px;background:var(--blue-hero);color:var(--white)}
.hero h1{position:absolute;left:16px;top:112px;font-size:39px;font-weight:500;letter-spacing:.3px}
.hero h2{position:absolute;left:18px;top:158px;font-size:24px;font-weight:300}
.hero p{position:absolute;left:18px;top:189px;width:345px;font-size:12px;line-height:16px;font-weight:400}
.dots{position:absolute;left:21px;top:332px;display:flex;gap:5px}
.dots span{width:8px;height:8px;border-radius:50%;background:#1f3f5a}
.dots span:first-child{background:#3a7fb8}
.photo-a{position:absolute;left:496px;top:13px;width:246px;height:169px;background:linear-gradient(135deg,#c9d8e6,#6f92b8 55%,#e9ecef)}
.photo-b{position:absolute;left:373px;top:193px;width:248px;height:166px;background:linear-gradient(120deg,#20314f,#7e8fa8 50%,#c9cfd7)}

/* categories */
.cat{top:505px;width:176px;height:180px;overflow:hidden}
.cat .label{position:absolute;left:0;bottom:0;width:100%;height:37px;background:var(--blue-band);color:var(--white);font-size:20px;font-weight:400;text-align:center;line-height:39px}
.cat-1{left:63px;background:linear-gradient(180deg,#d9dee3,#52525a 60%,#2c2c33)}
.cat-2{left:258px;background:linear-gradient(160deg,#9a8576,#6b7f86 55%,#3b6e7c)}
.cat-3{left:451px;background:linear-gradient(150deg,#6d5b6e,#b89089 50%,#4b5a78)}
.cat-4{left:644px;background:linear-gradient(140deg,#8a6e55,#c9b8a3 50%,#5c6a80)}

/* action cards */
.card{top:719px;height:192px;text-align:center;color:var(--white)}
.card svg{position:absolute;left:50%;top:32px;transform:translateX(-50%)}
.card h3{position:absolute;left:0;width:100%;font-size:23px;font-weight:300}
.card .sub{position:absolute;left:0;width:100%;font-size:12px;font-weight:400}
.card .go{position:absolute;left:50%;transform:translateX(-50%);width:55px;height:21px;font-size:12px;line-height:21px;color:var(--ink)}
.card-call{left:63px;width:236px;background:var(--green)}
.card-call h3{top:82px}.card-call .sub{top:112px}.card-call .go{top:138px;background:var(--green-btn)}
.card-sign{left:324px;width:237px;background:var(--blue-card)}
.card-sign h3{top:85px}.card-sign .sub{top:115px}.card-sign .go{top:141px;background:var(--sky-btn)}
.card-news{left:584px;width:236px;background:var(--yellow);color:var(--ink)}
.card-news h3{top:83px}.card-news .sub{top:113px}.card-news .go{top:139px;background:var(--yellow-btn)}

/* info footer */
.info{left:0;top:951px;width:879px;height:200px;background:var(--white)}
.info h4{position:absolute;font-size:17px;font-weight:300;color:var(--ink)}
.reach-row{position:absolute;left:62px;display:flex;align-items:flex-start;gap:8px;font-size:11px;line-height:13px;color:var(--ink)}
.news-title{position:absolute;left:323px;top:22px;width:200px;font-size:17px;font-weight:300;line-height:21px}
.news-date{position:absolute;left:323px;top:66px;font-size:8px;color:var(--blue-strong)}
.news-body{position:absolute;left:323px;top:86px;width:195px;font-size:10px;line-height:12.5px;color:var(--ink)}
.read-more{position:absolute;left:323px;top:162px;display:flex;align-items:center;gap:8px;font-size:9px}
.read-more span.dot{width:18px;height:18px;border-radius:50%;background:#2f78c4;display:flex;align-items:center;justify-content:center}
.field{position:absolute;background:var(--field);font-size:9px;color:var(--ink);padding:7px 6px}
.submit{position:absolute;left:585px;top:160px;width:58px;height:17px;border:1px solid #5a8bc2;font-size:9px;text-align:center;line-height:15px;background:var(--white)}

/* bottom bar */
.bottom{left:0;top:1151px;width:879px;height:49px;background:var(--page);font-size:9px;color:var(--ink)}
.bottom .copy{position:absolute;left:63px;top:21px}
.bottom .links{position:absolute;right:59px;top:21px}
</style>
</head>
<body>

<div class="abs top-bar">
  <div class="abs promo">Pop-up your own ZORVA Boulevard for ONLY $99</div>
  <span class="abs social" style="left:680px"></span>
  <span class="abs social" style="left:700px"></span>
  <div class="abs login">STYLIST LOGIN</div>
</div>

<nav class="abs nav">
  <a class="active" href="#">Home</a>
  <a href="#">Get to know us</a>
  <a href="#">Why Zorva</a>
  <a href="#">Host a pop-up</a>
  <a href="#">Become a stylist</a>
  <a href="#">Contact us</a>
</nav>
<div class="abs brand">ZORVA<br>LANE</div>

<section class="abs hero">
  <h1>LIMITED INVENTORY</h1>
  <h2>That’s only available for ONE Week!</h2>
  <p>Lorem Ipsum is simply dummy text of the printing and typesetting industry. Lorem Ipsum has been the industry's standard dummy text ever since the 1500s.</p>
  <div class="dots"><span></span><span></span><span></span></div>
  <div class="photo-a" role="img" aria-label="Denim jackets hanging on a rail"></div>
  <div class="photo-b" role="img" aria-label="Shirts and tops on hangers"></div>
</section>

<div class="abs cat cat-1" role="img" aria-label="Friends wearing winter jackets"><div class="label">JACKETS</div></div>
<div class="abs cat cat-2" role="img" aria-label="Women in sweaters sharing coffee"><div class="label">SWEATERS</div></div>
<div class="abs cat cat-3" role="img" aria-label="Blurred clothing store racks"><div class="label">ZORVA SPECIALS</div></div>
<div class="abs cat cat-4" role="img" aria-label="Belts, watch and wallet accessories"><div class="label">ACCESSORIES</div></div>

<div class="abs card card-call">
  <svg width="40" height="40" viewBox="0 0 40 40"><path d="M10 4h8l3 9-5 3c2 5 5 8 10 10l3-5 9 3v8c0 2-2 4-4 4C17 36 4 23 4 8c0-2 2-4 6-4z" fill="#fff"/></svg>
  <h3>Call Now</h3><div class="sub">For Any Assistance</div><div class="go">Go</div>
</div>
<div class="abs card card-sign">
  <svg width="44" height="44" viewBox="0 0 44 44"><rect x="6" y="3" width="26" height="34" rx="2" fill="none" stroke="#fff" stroke-width="3"/><path d="M12 12h14M12 18h14M12 24h8" stroke="#fff" stroke-width="3"/><circle cx="31" cy="31" r="9" fill="#fff"/><path d="M26 31l4 4 6-7" stroke="#39a5d8" stroke-width="2.5" fill="none"/></svg>
  <h3>Signup</h3><div class="sub">As a Stylist</div><div class="go">Go</div>
</div>
<div class="abs card card-news">
  <svg width="44" height="40" viewBox="0 0 44 40"><path d="M10 4h26v26c0 4-3 6-6 6H6c3 0 4-2 4-5z" fill="#fff"/><path d="M16 11h14M16 17h14M16 23h10" stroke="#f0b43a" stroke-width="2"/></svg>
  <h3>News &amp; Updates</h3><div class="sub">Get to know more about us</div><div class="go">Go</div>
</div>

<section class="abs info">
  <h4 style="left:62px;top:22px">Reach Us</h4>
  <div class="reach-row" style="top:60px">
    <svg width="20" height="22" viewBox="0 0 20 22"><path d="M10 1a7 7 0 0 0-7 7c0 5 7 13 7 13s7-8 7-13a7 7 0 0 0-7-7z" fill="none" stroke="var(--icon)" stroke-width="1.5"/><circle cx="10" cy="8" r="2.5" fill="var(--icon)"/></svg>
    <span>2870 Lakeview Hollow Road, Suite 310,<br>Chicago, IL</span>
  </div>
  <div class="reach-row" style="top:111px">
    <svg width="20" height="20" viewBox="0 0 20 20"><circle cx="10" cy="10" r="9" fill="none" stroke="var(--icon)" stroke-width="1.5"/><rect x="5" y="7" width="10" height="7" fill="none" stroke="var(--icon)"/><path d="M5 7l5 4 5-4" fill="none" stroke="var(--icon)"/></svg>
    <span style="padding-top:4px">info@zorvalane.com</span>
  </div>
  <div class="reach-row" style="top:150px">
    <svg width="20" height="22" viewBox="0 0 20 22"><rect x="5" y="3" width="10" height="17" rx="1.5" fill="none" stroke="var(--icon)" stroke-width="1.5"/><rect x="7" y="6" width="6" height="6" fill="var(--icon)"/></svg>
    <span style="padding-top:4px">(+1) 312 555 0148</span>
  </div>

  <div class="news-title">Lorem Ipsum is simply dummy text</div>
  <div class="news-date">28 May 2017</div>
  <div class="news-body">There are many variations of passages of Lorem Ipsum available, but the majority have suffered alteration in some form, by injected humour, or randomised words which don't look even slightly believable.</div>
  <div class="read-more"><span class="dot"><svg width="8" height="8" viewBox="0 0 8 8"><path d="M1 4h6M4 1l3 3-3 3" stroke="#fff" fill="none"/></svg></span>Read Full Story</div>

  <h4 style="left:583px;top:22px">Contact Us</h4>
  <div class="field" style="left:585px;top:49px;width:115px;height:24px">Name</div>
  <div class="field" style="left:703px;top:49px;width:117px;height:24px">Company</div>
  <div class="field" style="left:585px;top:77px;width:115px;height:24px">Phone #</div>
  <div class="field" style="left:703px;top:77px;width:117px;height:24px">Email</div>
  <div class="field" style="left:585px;top:104px;width:235px;height:52px">Subject</div>
  <div class="submit">Submit</div>
</section>

<footer class="abs bottom">
  <div class="copy">© 2018 ZORVA lane &nbsp;|&nbsp; All rights reserved.</div>
  <div class="links">Home | About Us | Contact Us</div>
</footer>

</body>
</html>
```